Zielgruppe
Wir sind ein Liechtensteiner Personaldienstleisungsunternehmen welches sowohl in der klassischen Personalvermittlung als auch in der temporären Personalbereitstellung tätig ist. Unsere Branchen reichen von Baugewerbe, Handwerk, Gastro- und Hotelerie bis hin zu Produktion und Gesundheitswesen.
Achtung:
Habe gerade die files vom neuen Logo hochgeladen!!!
Aufgabenstellung
Visitienkarten designen.
Briefpapier Vorlagenerstellung.
Schlichtes Visitenkartendesign Business auf der nicht zuviele Informationen sind (das Wichtigste)
Vorderseite:
Logo (wird vor Abschluss noch in besserer Qualität hochgeladen)
Firmenname
Anschrift
Name
Funktion
Telefon
Fax
E-Mail
Homepage
Rückseite:
Kann Kreativ gestaltet werden, farblich (blau, gelb, schwarz, weiss), nach Möglichkeit keinen weissen Hintergrund.
!!Bitte keine Vorschläge mit dem Fotoscanner ... da! Danke.
Wir freuen uns auch auf kreative Vorschläge, welche etwas vom Briefing abweichen.
TKV - Team

```html
<!DOCTYPE html>
<html lang="de">
<head>
<meta charset="utf-8">
<title>TKV Personal – Geschäftsausstattung</title>
<link rel="stylesheet" href="https://fonts.googleapis.com/css2?family=Source+Sans+3:wght@400;600;700&display=swap">
<style>
:root{
  --blue:#2a5bc0;
  --blue-dark:#1f47a3;
  --yellow:#f2d400;
  --ink:#1d1d1d;
  --grey:#6b6b6b;
  --paper:#ffffff;
  --stage:#ececee;
}
*{margin:0;padding:0;box-sizing:border-box}
html,body{width:1200px;height:900px;overflow:hidden;background:var(--stage);font-family:"Source Sans 3",Arial,sans-serif;color:var(--ink)}
.canvas{position:relative;width:1200px;height:900px}

/* Letterhead */
.letterhead{position:absolute;left:70px;top:60px;width:560px;height:780px;background:var(--paper);box-shadow:0 6px 18px rgba(0,0,0,.12)}
.brand{font-weight:700;color:var(--blue);letter-spacing:.02em}
.letterhead .brand{position:absolute;right:44px;top:46px;font-size:30px}
.recipient{position:absolute;left:70px;top:150px;font-size:10px;line-height:1.35;font-style:normal}
.recipient strong{font-weight:700}
.date{position:absolute;right:44px;top:250px;font-size:10px}
.subject{position:absolute;left:70px;top:280px;font-size:10.5px;font-weight:700}
.body{position:absolute;left:70px;top:310px;width:446px;font-size:9.5px;line-height:1.45}
.body p{margin-bottom:9px}
.closing{margin-top:14px}
.signer{margin-top:30px}
.signer small{display:block;font-size:7.5px;color:var(--grey)}
.fold-mark{position:absolute;left:18px;width:10px;height:1px;background:#888}
.fold-mark.top{top:262px}
.fold-mark.low{top:390px}
.lh-footer{position:absolute;left:0;bottom:0;width:100%;height:130px;border-top:2px solid var(--yellow)}
.lh-footer .band{position:absolute;left:0;top:76px;width:100%;height:52px;background:var(--blue);color:#fff;font-size:9px;padding:20px 70px 0}
.lh-cols{display:flex;justify-content:space-between;padding:12px 70px 0;font-size:7.5px;line-height:1.4;color:var(--ink)}
.lh-cols dl{display:grid;grid-template-columns:auto auto;column-gap:8px}

/* Cards */
.card{position:absolute;left:700px;width:420px;height:254px;box-shadow:0 6px 18px rgba(0,0,0,.14)}
.card-front{top:110px;background:var(--paper)}
.card-front .brand{position:absolute;left:30px;top:30px;font-size:26px}
.card-front .person{position:absolute;left:30px;top:104px}
.person .name{font-size:17px;font-weight:700;color:var(--blue)}
.person .role{font-size:9px;color:var(--grey)}
.card-contact{position:absolute;font-size:9px;line-height:1.5;display:grid;grid-template-columns:auto auto;column-gap:10px}
.card-contact dt{color:var(--blue)}
.card-contact.mobile{left:30px;top:154px}
.card-contact.office{right:30px;top:40px;border-left:1px solid var(--blue);padding-left:10px}
.card-footer{position:absolute;left:0;bottom:0;width:100%;height:34px;background:var(--blue);border-top:2px solid var(--yellow);color:#fff;font-size:8.5px;padding:11px 30px 0}
.card-footer b{font-weight:700}

.card-back{top:420px;background:var(--blue)}
.card-back .pattern{position:absolute;inset:0;background:linear-gradient(135deg,var(--blue) 0%,var(--blue-dark) 100%)}
.card-back .stripe{position:absolute;top:0;bottom:0;right:36px;width:2px;background:var(--yellow)}
.card-back .brand{position:absolute;left:34px;bottom:30px;font-size:24px;color:#fff}
.card-back .web{position:absolute;right:50px;bottom:30px;font-size:9px;color:#fff}
</style>
</head>
<body>
<main class="canvas">

  <article class="letterhead">
    <div class="brand">TKV Personal</div>

    <address class="recipient">
      <strong>Musterfirma GmbH</strong><br>
      Max Mustermann<br>
      Musterstraße 10a<br><br>
      D – 012345 Musterstadt
    </address>

    <span class="fold-mark top"></span>
    <span class="fold-mark low"></span>

    <div class="date">Musterstadt, den 01.01.2013</div>
    <div class="subject">Betreff: Irgendein Betrefftext wird dann hier stehen oder vielleicht auch nicht</div>

    <div class="body">
      <p>Sehr geehrte Damen und Herren,</p>
      <p>Lorem ipsum dolor sit amet, consectetur adipiscing elit, sed do eiusmod tempor incididunt ut labore et dolore magna aliqua. Ut enim ad minim veniam, quis nostrud exercitation ullamco laboris nisi ut aliquip ex ea commodo consequat. Duis aute irure dolor in reprehenderit in voluptate velit esse cillum dolore eu fugiat nulla pariatur. Excepteur sint occaecat cupidatat non proident, sunt in culpa qui officia deserunt mollit anim id est laborum.</p>
      <p>Bis nostrud exercitation ullam mmodo consequat. Duis aute in voluptate velit esse cillum dolore eu fugiat nulla pariatur. At vver eos et accusam dignissum qui blandit est praesent luptatum delenit aigue excepteur sint occae. Et harumd dereud facilis est er expedit distinct. Nam liber te conscient to factor tum poen legum odioque civiuda.</p>
      <p>Irure dolor in reprehend incididunt ut labore et dolore magna aliqua. Ut enim ad minim veniam, quis nostrud exercitation ullamco laboris nisi ut aliquip ex ea commodo consequat. Duis aute irure dolor in reprehenderit in voluptate velit esse molestaie cillum.</p>
      <p>At vver eos et accusam dignissum qui blandit est praesent. Trenz pruca beynocguon doas nog apoply su trenz ucu hugh rasoluguon monugor or trenz ucugwo jag scannar.</p>
      <p class="closing">Mit freundlichen Grüßen</p>
      <p class="signer">Lukas Brenner<small>Geschäftsführer</small></p>
    </div>

    <footer class="lh-footer">
      <div class="lh-cols">
        <dl><dt>Tel:</dt><dd>+423 555 20 10</dd><dt>Fax:</dt><dd>+423 555 20 11</dd><dt>E-Mail:</dt><dd>office@tkv.li</dd><dt>Web:</dt><dd>www.tkv.li</dd></dl>
        <div>Alpenbank Nord<br>Inhaber: Lukas Brenner<br>BLZ: 880 450 20<br>KTO: 204 518 733 00</div>
        <div>IBAN: LI2108800000123456789<br>BIC: ALPNLI22<br>Steuer-Nr.: 47 / 318 / 90215<br>Mobil: +43 660 418 27 09</div>
      </div>
      <div class="band"><b>TKV Anstalt</b> | Talgasse 14 | 9493 Mauren | Liechtenstein</div>
    </footer>
  </article>

  <section class="card card-front">
    <div class="brand">TKV Personal</div>
    <div class="person">
      <div class="name">Lukas Brenner</div>
      <div class="role">Geschäftsführer</div>
    </div>
    <dl class="card-contact mobile"><dt>Mobil:</dt><dd>+43 660 418 27 09</dd><dt>E-Mail:</dt><dd>lukas.brenner@tkv.li</dd></dl>
    <dl class="card-contact office"><dt>Tel:</dt><dd>+423 555 20 10</dd><dt>Fax:</dt><dd>+423 555 20 11</dd><dt>E-Mail:</dt><dd>office@tkv.li</dd><dt>Web:</dt><dd>www.tkv.li</dd></dl>
    <div class="card-footer"><b>TKV Anstalt</b> | Talgasse 14 | 9493 Mauren | Liechtenstein</div>
  </section>

  <section class="card card-back">
    <div class="pattern" role="img" aria-label="Blaues Flächenmuster aus wiederholten Figuren"></div>
    <span class="stripe"></span>
    <div class="brand">TKV Personal</div>
    <div class="web">www.tkv.li</div>
  </section>

</main>
</body>
</html>
```